Technology Project Portal - Project Listing portal

We require a logo & website designed for our new project.

Project Name: lumrik
Description:
We have a webapp where clients and service providers can come, signup and register development projects. Service providers can the browse projects and contact clients via the portal

Design brief:
Clean & Modern - See Attached color palet & style references. (Feel free to try alternative color palets)

See Project Proposal for site requirements.
UX flow section details pages requires

Examples of all standard UI Components required e.g.
text box / field
Drop down
date picker
etc..
Updates

Target Market(s)

Business / Technology providers

Logo Text

LumRik

Coding

Coded - Design and coding required

Number of Pages Required

5+ page

Requirements
Must have
• Clean Modern Design
Examples for all common UI elements
Templates for common Web App Dialogs e.g. Confirm Delete/Logout etc

```html
<!DOCTYPE html>
<html lang="en">
<head>
<meta charset="utf-8">
<title>LumRik</title>
<link rel="stylesheet" href="https://fonts.googleapis.com/css2?family=Montserrat:wght@300;400;500;600&display=swap">
<style>
  :root {
    --brand-blue: #34499f;
    --brand-blue-deep: #2b3d8a;
    --brand-red: #ef4324;
    --brand-red-deep: #d8391d;
    --ink: #4a4a4c;
    --ink-dark: #2f2f31;
    --muted: #8c8d90;
    --panel-light: #bcbdc0;
    --panel-dark: #77787c;
    --footer: #3f3f42;
    --footer-head: #a9aaad;
    --white: #ffffff;
    --line: #9a9a9c;
  }
  * { margin: 0; padding: 0; box-sizing: border-box; }
  html, body { width: 1200px; height: 2931px; overflow: hidden; background: var(--white); }
  body { position: relative; font-family: "Montserrat", sans-serif; color: var(--ink); }
  .abs { position: absolute; }

  .hero-mark { left: 0; width: 1200px; top: 420px; text-align: center; font-size: 92px; font-weight: 500; color: var(--brand-blue); letter-spacing: -1px; }

  .site { left: 0; top: 882px; width: 1200px; height: 2049px; }
  .site-header { left: 0; top: 882px; width: 1200px; height: 382px; border: 1px solid var(--line); border-bottom: none; }
  .site-logo { left: 38px; top: 948px; font-size: 34px; font-weight: 500; color: var(--brand-blue); }
  .site-logo::before { content: ""; position: absolute; left: 58px; top: -34px; width: 22px; height: 22px; background: var(--brand-red); }

  .search { left: 586px; top: 929px; width: 165px; height: 27px; border: 1px solid #8b8b8d; display: flex; align-items: center; }
  .search-icon { width: 26px; height: 100%; background: #8b8b8d; display: flex; align-items: center; justify-content: center; }
  .search-text { font-size: 12px; color: #a0a0a2; padding-left: 10px; letter-spacing: 0.5px; }
  .nav { top: 933px; font-size: 16px; font-weight: 400; color: #6a6a6c; }

  .headline { left: 0; width: 1200px; top: 1012px; text-align: center; font-size: 45px; font-weight: 500; line-height: 64px; color: #555557; }
  .subline { left: 0; width: 1200px; top: 1214px; text-align: center; font-size: 24px; font-weight: 300; color: #7e7f82; letter-spacing: 0.6px; }

  .band { top: 1264px; height: 232px; }
  .band-clients { left: 0; width: 600px; background: linear-gradient(160deg, #3b53a8 0%, var(--brand-blue) 45%, var(--brand-blue-deep) 100%); }
  .band-contractors { left: 600px; width: 600px; background: linear-gradient(200deg, #e55a3c 0%, var(--brand-red) 45%, var(--brand-red-deep) 100%); }
  .band-title { position: absolute; width: 100%; top: 72px; text-align: center; color: var(--white); font-size: 70px; font-weight: 500; letter-spacing: -0.5px; }

  .panel { top: 1496px; height: 521px; }
  .panel-clients { left: 0; width: 600px; background: linear-gradient(150deg, #c3c4c7 0%, var(--panel-light) 50%, #b3b4b7 100%); }
  .panel-contractors { left: 600px; width: 600px; background: linear-gradient(210deg, #808185 0%, var(--panel-dark) 55%, #6f7074 100%); }
  .panel-copy { position: absolute; top: 22px; font-size: 17.5px; line-height: 22px; font-weight: 400; }
  .panel-clients .panel-copy { left: 38px; color: #7a7b7e; }
  .panel-contractors .panel-copy { left: 35px; color: var(--white); }
  .panel-copy p + p { margin-top: 22px; }
  .benefits { position: absolute; list-style: none; font-size: 24px; font-weight: 300; line-height: 37px; }
  .panel-clients .benefits { left: 38px; top: 148px; color: var(--white); }
  .panel-contractors .benefits { left: 35px; top: 268px; color: #b9babd; }

  .testimonial { left: 0; top: 2017px; width: 1200px; height: 366px; border-left: 1px solid var(--line); border-right: 1px solid var(--line); }
  .arrow { top: 2104px; }
  .portrait { left: 288px; top: 2105px; width: 170px; height: 170px; border-radius: 50%; background: radial-gradient(circle at 50% 35%, #d9c2ad 0%, #6b7285 45%, #1f2638 100%); }
  .quote { left: 499px; top: 2092px; font-size: 33px; font-weight: 500; line-height: 38px; color: #8e8f92; letter-spacing: 2px; }
  .quote .mark { color: var(--brand-red); }
  .quote-name { left: 499px; top: 2195px; font-size: 25px; font-weight: 600; color: #4b4b4d; letter-spacing: 2px; }
  .quote-role { left: 499px; top: 2229px; font-size: 16px; font-weight: 300; color: #8e8f92; letter-spacing: 1px; }

  .info { left: 0; top: 2383px; width: 1200px; height: 205px; background: var(--panel-light); }
  .info-col { position: absolute; top: 44px; }
  .info-col h3 { font-size: 31px; font-weight: 500; color: var(--ink-dark); line-height: 36px; }
  .info-col p { margin-top: 4px; font-size: 20px; font-weight: 300; line-height: 24.5px; color: var(--white); }

  .footer { left: 0; top: 2588px; width: 1200px; height: 343px; background: var(--footer); }
  .footer-square { left: 32px; top: 185px; width: 127px; height: 127px; background: #d2d3d5; }
  .footer-col { position: absolute; top: 37px; }
  .footer-col h4 { font-size: 22px; font-weight: 400; color: var(--footer-head); line-height: 28px; margin-bottom: 18px; }
  .footer-col ul { list-style: none; margin-left: 2px; }
  .footer-col li { font-size: 15px; font-weight: 400; color: var(--white); line-height: 30px; }
</style>
</head>
<body>

  <div class="abs hero-mark">LumRik</div>

  <header class="abs site-header"></header>
  <div class="abs site-logo">LumRik</div>

  <div class="abs search">
    <div class="search-icon">
      <svg width="16" height="16" viewBox="0 0 16 16"><circle cx="6.5" cy="6.5" r="4.5" fill="none" stroke="#fff" stroke-width="2"/><line x1="10" y1="10" x2="14.5" y2="14.5" stroke="#fff" stroke-width="2.5"/></svg>
    </div>
    <span class="search-text">Search</span>
  </div>
  <nav>
    <span class="abs nav" style="left:781px">Register</span>
    <span class="abs nav" style="left:881px">Login</span>
    <span class="abs nav" style="left:969px">Testimonials</span>
    <span class="abs nav" style="left:1094px">Services</span>
  </nav>

  <h1 class="abs headline">“An Agent helping you out with your<br>Project May not be the Best Thing you<br>are looking for.”</h1>
  <p class="abs subline">Get rid of the Middleman in Between and Take complete control over your possibilities</p>

  <section class="abs band band-clients"><h2 class="band-title">Clients</h2></section>
  <section class="abs band band-contractors"><h2 class="band-title">Contractors</h2></section>

  <div class="abs panel panel-clients">
    <div class="panel-copy">
      <p>With lumrik, you as a business can get access to a pool<br>of talent, without the need for the middleman. Reducing<br>costs, improving transparency andmaking business<br>arrangements directly with the service providers.</p>
    </div>
    <ul class="benefits">
      <li>No recurring Agent fees</li>
      <li>Direct contact with vetted &amp; talented service<br>providers.</li>
      <li>Flexible terms to match your project</li>
      <li>Visibility of available service providers, allowing<br>future planning of projects</li>
      <li>See the talent pool, not a subset</li>
    </ul>
  </div>

  <div class="abs panel panel-contractors">
    <div class="panel-copy">
      <p>Take control of your business, by taking away the need<br>for agents. Top service providers do *not* need an agent.<br>Your talent can sell itself, lumrik puts you in front of<br>potential clients without the smoke screen thrown up by<br>agents.</p>
      <p>LumRik gives you as a service provider access to<br>projects, that match your skill set. Browse the curated list<br>of available and up-coming projects that have been<br>selected based on your skills. Register interest, notify</p>
    </div>
    <ul class="benefits">
      <li>Reach potential clients directly</li>
      <li>See project outlines, from the start. Only register<br>interest in projects you wish</li>
      <li>Take short term gigs, to large scale projects</li>
      <li>Set your rate and terms without an Agent</li>
    </ul>
  </div>

  <section class="abs testimonial"></section>
  <svg class="abs arrow" style="left:76px" width="84" height="168" viewBox="0 0 84 168"><polyline points="82,2 4,84 82,166" fill="none" stroke="var(--brand-blue)" stroke-width="7"/></svg>
  <svg class="abs arrow" style="left:1036px" width="84" height="168" viewBox="0 0 84 168"><polyline points="2,2 80,84 2,166" fill="none" stroke="var(--brand-blue)" stroke-width="7"/></svg>
  <div class="abs portrait" role="img" aria-label="Portrait photo of a smiling businessman in a dark suit"></div>
  <blockquote class="abs quote"><span class="mark">“</span>A Great and Convenient<br>Way to Work with.<span class="mark">”</span></blockquote>
  <div class="abs quote-name">Marcus Vell</div>
  <div class="abs quote-role">Tried to Work at Placely</div>

  <section class="abs info">
    <div class="info-col" style="left:96px"><h3>About Us</h3><p>We are the<br>people who do<br>this...</p></div>
    <div class="info-col" style="left:317px"><h3>Who We Are</h3><p>We started off as<br>something of this<br>sort...</p></div>
    <div class="info-col" style="left:566px"><h3>Why We do This</h3><p>While doing something<br>of this sort we seemed...</p></div>
    <div class="info-col" style="left:878px"><h3>Find Out more</h3><p>Not sure if you know<br>everything? Click to find<br>out more.</p></div>
  </section>

  <footer class="abs footer">
    <div class="abs footer-square"></div>
    <div class="footer-col" style="left:259px"><h4>Clients</h4>
      <ul><li>See Feasibility</li><li>See possibilities</li><li>Screen Candidates</li><li>Find out More</li><li>See Testimonials</li><li>FAQ</li><li>Register</li><li>Login</li></ul></div>
    <div class="footer-col" style="left:456px"><h4>Contractors</h4>
      <ul><li>See Feasibility</li><li>See possibilities</li><li>Screen Candidates</li><li>Find out More</li><li>See Testimonials</li><li>FAQ</li><li>Register</li><li>Login</li></ul></div>
    <div class="footer-col" style="left:685px"><h4>The Company</h4>
      <ul><li>See Feasibility</li><li>See possibilities</li><li>Screen Candidates</li><li>Find out More</li><li>See Testimonials</li><li>FAQ</li><li>Register</li><li>Login</li></ul></div>
    <div class="footer-col" style="left:926px"><h4>Other Resources</h4>
      <ul><li>See Feasibility</li><li>See possibilities</li><li>Screen Candidates</li><li>Find out More</li><li>See Testimonials</li><li>FAQ</li><li>Register</li><li>Login</li></ul></div>
  </footer>

</body>
</html>
```